Long term Care Provider Conference

Banner for LTC providers to know that they can rely on us to deliver high value, cost efficient, professional back office support to streamline operations, improve and maintain compliance with administrative and or nursing solutions for their agency.

Want to update the wording

```html
<!DOCTYPE html>
<html lang="en">
<head>
<meta charset="utf-8">
<title>Healthcare VA Solutions Banner</title>
<link rel="stylesheet" href="https://fonts.googleapis.com/css2?family=Poppins:wght@400;500;600;700;800&display=swap">
<style>
  :root {
    --stage: #35373a;
    --paper: #ffffff;
    --teal: #528f96;
    --teal-deep: #4a8b92;
    --ink: #2f3236;
    --taupe: #cfc3bd;
  }
  * { margin: 0; padding: 0; box-sizing: border-box; }
  html, body { width: 1200px; height: 2400px; overflow: hidden; }
  body {
    background: var(--stage);
    font-family: "Poppins", sans-serif;
    color: var(--ink);
    position: relative;
  }
  .banner {
    position: absolute;
    left: 50px; top: 600px;
    width: 1100px; height: 1200px;
    background: var(--paper);
    overflow: hidden;
  }
  .banner-shapes { position: absolute; inset: 0; }
  .headline { position: absolute; left: 56px; top: 72px; }
  .headline-kicker {
    font-size: 33px; font-weight: 500; letter-spacing: 11px;
    line-height: 1; margin-bottom: 6px;
  }
  .headline-focus {
    font-size: 89px; font-weight: 700; color: var(--teal-deep);
    line-height: 1.04; letter-spacing: -1px;
  }
  .headline-rest { font-size: 62px; line-height: 1.03; }
  .headline-rest .light { font-weight: 400; }
  .headline-rest .bold { font-weight: 700; }
  .headline-rest .heavy { font-weight: 800; }
  .pill {
    position: absolute; display: flex; align-items: center;
    border-radius: 36px; font-weight: 700; font-size: 36px;
    letter-spacing: 0.5px;
  }
  .pill svg { width: 34px; height: 34px; margin: 0 20px 0 24px; }
  .pill-value { left: 59px; top: 529px; width: 388px; height: 71px; background: var(--taupe); color: var(--ink); }
  .pill-cost { left: 55px; top: 616px; width: 403px; height: 68px; background: var(--ink); color: var(--paper); }
  .brand {
    position: absolute; left: 640px; top: 76px;
    display: flex; align-items: center; gap: 14px;
  }
  .brand-dot { width: 70px; height: 70px; border-radius: 50%; background: var(--teal); flex: none; }
  .brand-name {
    font-size: 40px; font-weight: 600; color: var(--ink); line-height: 1.05;
  }
  .feature {
    position: absolute; top: 795px; display: flex; align-items: center; gap: 16px;
    color: var(--paper); font-size: 22.5px; line-height: 1.2; font-weight: 400;
  }
  .feature-icon {
    width: 74px; height: 74px; border-radius: 50%; background: var(--paper);
    display: flex; align-items: center; justify-content: center; flex: none;
  }
  .feature-icon svg { width: 42px; height: 42px; }
  .feature-backoffice { left: 55px; }
  .feature-compliance { left: 446px; }
  .web-address {
    position: absolute; left: 166px; top: 1003px; width: 767px; height: 79px;
    background: var(--paper); border-radius: 40px;
    display: flex; align-items: center; justify-content: center;
    font-size: 42px; font-weight: 700; letter-spacing: 8px; color: var(--ink);
    box-shadow: 0 6px 14px rgba(0,0,0,0.18);
  }
</style>
</head>
<body>
  <main class="banner">
    <svg class="banner-shapes" width="1100" height="1200" viewBox="0 0 1100 1200">
      <defs>
        <linearGradient id="footer-tone" x1="0" y1="0" x2="0" y2="1">
          <stop offset="0" stop-color="#528f96"/>
          <stop offset="1" stop-color="#5a9aa1"/>
        </linearGradient>
        <linearGradient id="photo-tone" x1="0" y1="0" x2="1" y2="1">
          <stop offset="0" stop-color="#5f6f74"/>
          <stop offset="0.45" stop-color="#c9cfd1"/>
          <stop offset="1" stop-color="#e9ebec"/>
        </linearGradient>
      </defs>
      <path class="footer-band" d="M0,752 C300,744 560,720 760,640 L1100,520 L1100,1200 L0,1200 Z" fill="url(#footer-tone)"/>
      <path class="accent-swoosh" d="M0,716 C260,712 520,698 740,640 C540,708 280,736 0,748 Z" fill="#2f3236"/>
      <circle class="accent-blob" cx="1012" cy="350" r="74" fill="#528f96"/>
      <circle class="photo-ring" cx="797" cy="503" r="290" fill="#ffffff"/>
      <circle class="photo" cx="797" cy="503" r="272" fill="url(#photo-tone)" role="img" aria-label="Photo of a smiling call-centre agent with headset working at a computer in a bright office"/>
    </svg>

    <header class="headline">
      <p class="headline-kicker">TRANSFORMING</p>
      <p class="headline-focus">Healthcare,</p>
      <p class="headline-rest">
        <span class="light">with</span> <span class="bold">expert</span><br>
        <span class="heavy">virtual</span><br>
        <span class="heavy">assistant</span><br>
        <span class="light">solutions</span>
      </p>
    </header>

    <div class="brand">
      <span class="brand-dot"></span>
      <span class="brand-name">Vitalis VA<br>Solutions</span>
    </div>

    <div class="pill pill-value">
      <svg viewBox="0 0 34 34"><circle cx="17" cy="17" r="14" fill="none" stroke="#ffffff" stroke-width="2.5"/><path d="M11 17.5l4 4 8-8" fill="none" stroke="#ffffff" stroke-width="2.5" stroke-linecap="round" stroke-linejoin="round"/></svg>
      HIGH VALUE
    </div>
    <div class="pill pill-cost">
      <svg viewBox="0 0 34 34"><circle cx="17" cy="17" r="14" fill="none" stroke="#528f96" stroke-width="2.5"/><path d="M11 17.5l4 4 8-8" fill="none" stroke="#528f96" stroke-width="2.5" stroke-linecap="round" stroke-linejoin="round"/></svg>
      COST EFFICIENT
    </div>

    <div class="feature feature-backoffice">
      <span class="feature-icon">
        <svg viewBox="0 0 42 42"><rect x="5" y="13" width="32" height="22" rx="3" fill="#2f3236"/><path d="M15 13v-4h12v4" fill="none" stroke="#2f3236" stroke-width="3"/></svg>
      </span>
      <p>We deliver professional<br>back office support to<br>streamline operations.</p>
    </div>
    <div class="feature feature-compliance">
      <span class="feature-icon">
        <svg viewBox="0 0 42 42"><rect x="8" y="6" width="26" height="32" rx="3" fill="#2f3236"/><path d="M21 14v12M15 20h12" stroke="#ffffff" stroke-width="3.5" stroke-linecap="round"/></svg>
      </span>
      <p>Improve and maintain<br>compliance with administrative<br>and or nursing solutions.</p>
    </div>

    <div class="web-address">www.vitalis-va.com</div>
  </main>
</body>
</html>
```